Bref créative
Business Cards - Skyline Assessors
Two sided business cards
Simple
Corwin Hask
Certified Appraiser
48270 Millbrook Lane #1174
Sterling, VA 20391
corwin@plumvexa.com
www.plumvexa.com
Just the logo, either include the text or not (what ever looks better)
Colors and Fonts Guide

```html
<!DOCTYPE html>
<html lang="en">
<head>
<meta charset="utf-8">
<title>Skyline Assessors – Business Card</title>
<link rel="stylesheet" href="https://fonts.googleapis.com/css2?family=PT+Sans:wght@400;700&display=swap">
<style>
  :root {
    --backdrop: #e9e6e1;
    --card: #ffffff;
    --brand-red: #a3191f;
    --brand-red-dark: #6e0f14;
    --brand-red-light: #d23a3f;
    --accent-blue: #2f6fa8;
    --ink: #2b2b2b;
    --ink-soft: #444444;
    --rule: #9a9a9a;
  }
  html, body {
    margin: 0;
    width: 1200px;
    height: 804px;
    overflow: hidden;
    background: var(--backdrop);
    font-family: "PT Sans", sans-serif;
  }
  .card {
    position: absolute;
    left: 100px;
    top: 117px;
    width: 1000px;
    height: 570px;
    background: var(--card);
    border-radius: 30px;
    overflow: hidden;
    box-shadow: 0 4px 14px rgba(0,0,0,0.18);
  }
  .edge-band {
    position: absolute;
    left: 0; top: 0; bottom: 0;
    width: 70px;
    background: linear-gradient(90deg, var(--brand-red-dark) 0%, var(--brand-red-light) 45%, var(--brand-red) 75%, var(--brand-red-dark) 100%);
  }
  .edge-line-blue {
    position: absolute;
    top: 0; bottom: 0;
    left: 82px;
    width: 5px;
    background: var(--accent-blue);
  }
  .edge-line-dark {
    position: absolute;
    top: 0; bottom: 0;
    left: 95px;
    width: 4px;
    background: var(--brand-red-dark);
  }
  .brand {
    position: absolute;
    left: 130px;
    width: 320px;
    top: 262px;
    display: flex;
    align-items: center;
    justify-content: center;
    gap: 14px;
  }
  .brand-dot {
    width: 18px;
    height: 18px;
    border-radius: 50%;
    background: var(--brand-red);
    flex: none;
  }
  .brand-name {
    font-size: 36px;
    font-weight: 700;
    color: var(--brand-red);
    letter-spacing: 1px;
    white-space: nowrap;
  }
  .divider {
    position: absolute;
    left: 459px;
    top: 190px;
    width: 2px;
    height: 250px;
    background: var(--rule);
  }
  .contact {
    position: absolute;
    left: 511px;
    top: 140px;
    color: var(--ink);
  }
  .contact-name {
    font-size: 32px;
    font-weight: 700;
    margin: 0;
    line-height: 1.1;
  }
  .contact-title {
    font-size: 22px;
    margin: 4px 0 0;
    color: var(--ink-soft);
  }
  .contact-address {
    font-size: 21px;
    margin: 44px 0 0;
    line-height: 36px;
    font-style: normal;
  }
  .contact-list {
    list-style: none;
    margin: 4px 0 0;
    padding: 0;
    font-size: 21px;
    line-height: 36px;
  }
  .contact-list li {
    display: flex;
    align-items: center;
    gap: 12px;
  }
  .contact-list svg {
    width: 18px;
    height: 18px;
    flex: none;
  }
</style>
</head>
<body>
  <div class="card">
    <div class="edge-band"></div>
    <div class="edge-line-blue"></div>
    <div class="edge-line-dark"></div>

    <div class="brand">
      <span class="brand-dot"></span>
      <span class="brand-name">Skyline Assessors</span>
    </div>

    <div class="divider"></div>

    <div class="contact">
      <p class="contact-name">Corwin Hask</p>
      <p class="contact-title">Certified Appraiser</p>
      <address class="contact-address">48270 Millbrook Lane #1174<br>Sterling, VA 20391</address>
      <ul class="contact-list">
        <li>
          <svg viewBox="0 0 18 18" aria-hidden="true">
            <rect x="4" y="1" width="10" height="16" rx="2" fill="var(--brand-red)"/>
            <rect x="6" y="4" width="6" height="7" fill="#fff"/>
            <circle cx="9" cy="14" r="1.2" fill="#fff"/>
          </svg>
          <span>5550143392</span>
        </li>
        <li>
          <svg viewBox="0 0 18 18" aria-hidden="true">
            <rect x="1" y="3" width="16" height="12" rx="1.5" fill="var(--brand-red)"/>
            <path d="M2 4.5 L9 10 L16 4.5" fill="none" stroke="#fff" stroke-width="1.5"/>
          </svg>
          <span>corwin@plumvexa.com</span>
        </li>
        <li>
          <svg viewBox="0 0 18 18" aria-hidden="true">
            <circle cx="9" cy="9" r="8" fill="var(--brand-red)"/>
            <ellipse cx="9" cy="9" rx="3.5" ry="8" fill="none" stroke="#fff" stroke-width="1.2"/>
            <line x1="1" y1="9" x2="17" y2="9" stroke="#fff" stroke-width="1.2"/>
          </svg>
          <span>www.plumvexa.com</span>
        </li>
      </ul>
    </div>
  </div>
</body>
</html>
```